Boutique Health and Fitness Personal Training Studio

I would like to have a brochure designed which provides a detailed description of the services offered in my business.
I have personal training studio, We look after people from early 20's to 90's, healthy to very unhealthy.
We conduct:
A consultation
An assessment
A personalised program
Personalised training sessions
I would like to base the design around the colours of my logo (attached) and use some of (or all of) the images and information I have also attached.
I would be happy with your own images included also.

Target Market(s)

20 to 90 year olds

Industry/Entity Type

Business

Font styles to use
Serif
Sans Serif

Colors
9bcb3c
add136
cadf82
eaf2ce

Requirements
Must have
• Colour and images of fitness.
• 8.5x14 legal
• Tri fold
• 2 folds with 3 faces back n front
Nice to have
• The feeling of wellbeing
Should not have
• This is not a gym.
• It should have the feel of a private relaxed environment

```html
<!DOCTYPE html>
<html lang="en">
<head>
<meta charset="utf-8">
<title>Evergreen Wellness Studio – Tri-fold Brochure</title>
<link href="https://fonts.googleapis.com/css2?family=Open+Sans:wght@400;600;700&family=Oswald:wght@500;700&family=Roboto+Condensed:wght@700&display=swap" rel="stylesheet">
<style>
  :root{
    --stage:#6e4a2c;
    --green:#6b9b2a;
    --green-dark:#4f7c18;
    --green-light:#9bcb3c;
    --lime:#add136;
    --pale:#eaf2ce;
    --ink:#222;
    --grey-text:#333;
    --paper:#ffffff;
    --paper-grey:#eeeeee;
    --band-dark:#2e2e2e;
  }
  *{box-sizing:border-box;margin:0;padding:0}
  html,body{width:907px;height:1200px;overflow:hidden}
  body{background:var(--stage);font-family:"Open Sans",Arial,sans-serif;position:relative}
  .sheet{position:absolute;left:46px;width:818px;background:var(--paper);overflow:hidden}
  .sheet--outside{top:87px;height:495px}
  .sheet--inside{top:623px;height:497px}
  .panel{position:absolute;top:0;height:100%;width:273px;overflow:hidden}
  .panel--1{left:0}.panel--2{left:272px}.panel--3{left:546px;width:272px}
  .art{position:absolute;left:0;top:0;width:100%;height:100%}
  .copy{position:absolute;color:#fff}
  .copy h3{font-size:13.5px;font-weight:700;margin-bottom:5px}
  .copy p{font-size:8.6px;line-height:1.38}
  .brand{display:flex;align-items:center;gap:6px;color:var(--green);font-weight:600;font-size:15px;line-height:1.05}
  .brand-dot{width:16px;height:16px;border-radius:50%;background:var(--green-light);flex:none}

  /* outside – panel 1 */
  .sessions{left:31px;top:36px;width:225px}
  .sessions h3{margin-top:10px}
  .sessions h3:first-child{margin-top:0}
  .sessions .line{font-size:12.5px;margin:4px 0 0}
  .parking{position:absolute;left:31px;top:232px;width:216px;height:22px;border-radius:4px;background:var(--band-dark);
    color:var(--lime);font-family:"Roboto Condensed",Arial,sans-serif;font-weight:700;font-size:15px;text-align:center;line-height:22px}

  /* outside – panel 2 */
  .contact{left:0;top:80px;width:100%;text-align:center;color:var(--ink)}
  .contact .brand{justify-content:center;margin-left:-20px;margin-bottom:18px;font-size:16px}
  .contact .unit{font-weight:700;font-size:12.5px;line-height:1.35}
  .contact .street{font-size:9.5px;font-weight:600;margin-top:5px}
  .contact .call{font-weight:700;font-size:12px;margin-top:4px}
  .contact .call span{font-size:10px}
  .contact .visit{font-weight:700;font-size:12px;margin-top:4px}
  .contact .web{font-size:9px;font-weight:700}

  /* outside – panel 3 */
  .cover{right:22px;top:355px;text-align:right;color:var(--green-dark)}
  .cover .headline{font-family:"Oswald",Arial,sans-serif;font-weight:700;font-size:23px;color:var(--green);letter-spacing:.2px}
  .cover .sub{font-family:"Oswald",Arial,sans-serif;font-weight:500;font-size:15.5px;color:var(--ink);margin-top:2px}
  .cover .brand{justify-content:flex-end;margin-top:14px;font-size:16px}

  /* inside – panel 1 */
  .team{left:29px;top:282px;width:228px;color:var(--ink)}
  .team h3{color:var(--green-dark);font-size:13px;line-height:1.25;margin-bottom:10px}
  .team p{font-size:8.8px;line-height:1.4}
  .team .brand{margin-top:20px;margin-left:8px;font-size:15px}
  .foot-band{position:absolute;left:0;bottom:0;width:100%;height:18px;background:var(--band-dark)}

  /* inside – panel 2 & 3 */
  .process{left:27px;top:32px;width:228px}
  .process h3{margin-top:9px;margin-bottom:3px}
  .process h3:first-child{margin-top:0}
  .plan{left:24px;top:30px;width:228px}
  .plan h3{margin-top:22px}
  .plan h3:first-child{margin-top:0}
</style>
</head>
<body>

<!-- Outside -->
<section class="sheet sheet--outside" aria-label="Brochure outside">
  <div class="panel panel--1">
    <svg class="art" viewBox="0 0 273 495" preserveAspectRatio="none">
      <defs><linearGradient id="gPhysio" x1="0" y1="0" x2="1" y2="1"><stop offset="0" stop-color="#c83a35"/><stop offset=".5" stop-color="#d8d2cc"/><stop offset="1" stop-color="#5a4a40"/></linearGradient></defs>
      <rect width="273" height="495" fill="var(--green)"/>
      <path d="M0,270 Q190,250 273,420 L273,495 L0,495Z" fill="var(--paper)"/>
      <path d="M0,270 Q190,250 273,420" fill="none" stroke="var(--green-dark)" stroke-width="8"/>
      <g role="img" aria-label="Photo: trainer assisting a client with a back stretch in the studio">
        <path d="M0,286 Q175,268 250,495 L0,495Z" fill="url(#gPhysio)"/>
      </g>
      <circle cx="242" cy="328" r="12" fill="var(--green)" role="img" aria-label="Small leaf decoration"/>
    </svg>
    <div class="copy sessions">
      <h3>Your sessions</h3>
      <p>Training at the studio is professional and caring, but focused and challenging. Typically each session will take approximately 60 minutes. Training times can be organized to suit your needs with early mornings and evenings available.</p>
      <h3>The Cost</h3>
      <p class="line">$45 paid in blocks of 5 or 10 sessions</p>
      <h3>Health fund claimable</h3>
      <p class="line">Open 7 days</p>
    </div>
    <div class="parking">Ample private parking available</div>
  </div>

  <div class="panel panel--2">
    <svg class="art" viewBox="0 0 273 495" preserveAspectRatio="none">
      <defs>
        <linearGradient id="gPaper" x1="0" y1="0" x2="1" y2="0"><stop offset="0" stop-color="#dcdcdc"/><stop offset=".5" stop-color="#fafafa"/><stop offset="1" stop-color="#e4e4e4"/></linearGradient>
        <linearGradient id="gStill" x1="0" y1="0" x2="0" y2="1"><stop offset="0" stop-color="#e6e6e6"/><stop offset=".45" stop-color="#b9c4a8"/><stop offset=".75" stop-color="#7a8a4a"/><stop offset="1" stop-color="#8a5a36"/></linearGradient>
      </defs>
      <rect width="273" height="495" fill="url(#gPaper)"/>
      <g role="img" aria-label="Photo: fresh vegetables, dumbbells, a water bottle and a tape measure with a faint jogger behind">
        <rect x="0" y="250" width="273" height="245" fill="url(#gStill)"/>
      </g>
      <path d="M273,300 Q240,430 210,495 L273,495Z" fill="var(--green)"/>
    </svg>
    <div class="copy contact">
      <div class="brand"><span class="brand-dot"></span>Evergreen<br>Wellness Studio</div>
      <p class="unit">Unit 12<br>Level 2</p>
      <p class="street">18 Wattle Grove Lane Kellow</p>
      <p class="call">call-<span>0400 555 217</span></p>
      <p class="visit">vist us</p>
      <p class="web">www.evergreenwellness.example</p>
    </div>
  </div>

  <div class="panel panel--3">
    <svg class="art" viewBox="0 0 272 495" preserveAspectRatio="none">
      <defs><linearGradient id="gCable" x1="0" y1="0" x2="1" y2="1"><stop offset="0" stop-color="#9aa08a"/><stop offset=".5" stop-color="#b07a5c"/><stop offset="1" stop-color="#1c2a2c"/></linearGradient></defs>
      <rect width="272" height="495" fill="var(--paper)"/>
      <circle cx="150" cy="115" r="150" fill="var(--green)"/>
      <g role="img" aria-label="Photo: athletic man training on a cable machine">
        <circle cx="152" cy="110" r="140" fill="url(#gCable)"/>
      </g>
      <path d="M0,330 Q120,250 272,262 L272,280 Q120,275 0,350Z" fill="var(--green)"/>
      <circle cx="40" cy="270" r="14" fill="var(--green)" role="img" aria-label="Small leaf decoration"/>
    </svg>
    <div class="copy cover">
      <p class="headline">PERSONALISED CARE</p>
      <p class="sub">IN FITNESS AND HEALTH</p>
      <div class="brand"><span class="brand-dot"></span>Evergreen<br>Wellness Studio</div>
    </div>
  </div>
</section>

<!-- Inside -->
<section class="sheet sheet--inside" aria-label="Brochure inside">
  <div class="panel panel--1">
    <svg class="art" viewBox="0 0 273 497" preserveAspectRatio="none">
      <defs><linearGradient id="gTread" x1="0" y1="0" x2="1" y2="1"><stop offset="0" stop-color="#f2f2f2"/><stop offset=".5" stop-color="#b8c7d2"/><stop offset="1" stop-color="#55606a"/></linearGradient></defs>
      <rect width="273" height="497" fill="var(--paper-grey)"/>
      <circle cx="125" cy="105" r="150" fill="var(--green)"/>
      <g role="img" aria-label="Photo: woman exercising on a treadmill">
        <circle cx="120" cy="100" r="142" fill="url(#gTread)"/>
      </g>
      <circle cx="232" cy="248" r="14" fill="var(--green)" role="img" aria-label="Small leaf decoration"/>
    </svg>
    <div class="copy team">
      <h3>Experienced professionals caring<br>for your wellbeing</h3>
      <p>Evergreen Wellness Studio have had over 25 years of experience managing the health and fitness needs of the community. Exercise programs can be designed for all levels of health and fitness and all age groups. The Studio is managed by an <strong>Exercise Physiologist</strong> with expertise in caring for people with a wide range of challenging health conditions.</p>
      <div class="brand"><span class="brand-dot"></span>Evergreen<br>Wellness Studio</div>
    </div>
    <div class="foot-band"></div>
  </div>

  <div class="panel panel--2">
    <svg class="art" viewBox="0 0 273 497" preserveAspectRatio="none">
      <defs><linearGradient id="gYoga" x1="0" y1="0" x2="0" y2="1"><stop offset="0" stop-color="#e8b0c0"/><stop offset=".6" stop-color="#e7cdb8"/><stop offset="1" stop-color="#2b2b2b"/></linearGradient></defs>
      <rect width="273" height="497" fill="var(--green)"/>
      <g role="img" aria-label="Photo: smiling woman seated cross-legged holding a dumbbell and a plate of vegetables">
        <rect x="40" y="318" width="190" height="179" rx="80" fill="url(#gYoga)"/>
      </g>
    </svg>
    <div class="copy process">
      <h3>What to Expect</h3>
      <p>On arrival at the studio you will be asked to complete a questionnaire, which will provide us with information regarding your background with health and fitness, as well as your goals and objectives Please bring any relevant medical information from medical practitioners or health professionals that you feel may impact on your program.</p>
      <h3>Consultation</h3>
      <p>A consultation will allow you to share your thoughts, concerns and objectives, as well as provide you with ample opportunity to expand on the answers from your questionnaire relating to your prior and current health, medical and physical concerns.</p>
      <h3>Assessment</h3>
      <p>An assessment will be conducted to provide us both with a baseline measure of your cardiovascular fitness, strength, flexibility, balance and body composition measures. These measures provide us with a reference for program design and also to indicate improvements along the way.</p>
    </div>
  </div>

  <div class="panel panel--3">
    <svg class="art" viewBox="0 0 272 497" preserveAspectRatio="none">
      <defs><linearGradient id="gLunge" x1="0" y1="0" x2="1" y2="0"><stop offset="0" stop-color="#f4f4f4"/><stop offset=".55" stop-color="#3a3a3a"/><stop offset="1" stop-color="#1f3550"/></linearGradient></defs>
      <rect width="272" height="497" fill="var(--green)"/>
      <path d="M0,497 Q20,290 272,255 L272,497Z" fill="var(--green-dark)"/>
      <path d="M12,497 Q35,300 272,270 L272,497Z" fill="var(--paper)"/>
      <g role="img" aria-label="Photo: trainer guiding a woman through a lunge, shown in silhouette">
        <path d="M40,497 Q70,320 272,292 L272,497Z" fill="url(#gLunge)"/>
      </g>
    </svg>
    <div class="copy plan">
      <h3>The program</h3>
      <p>Your program will be designed with consideration to your health and fitness background, you objectives and your strengths and weaknesses. It will be personally tailored to your needs and provide you with a plan to focus your energies on.</p>
      <h3>Nutrition</h3>
      <p>Nutrition is central to an effective program, as it will provide you with maximal energy for exercise as well as keeping yourself lean and healthy for a long term fitter lifestyle. Evergreen Wellness Studio provides initial monitoring and ongoing modification in accordance with your needs.</p>
    </div>
  </div>
</section>

</body>
</html>
```